Need Landing Page for Data Security Company

Need a new landing page (PSD) for our data security company (www.korvadel.com). We specialize in selling patented hard drive destruction machines that guarantee the data on your hard drives are unrecoverable. We have several large clients such as Lumigrove, Chirpaloo and Vendrix just to name a few. Really want to have a landing page that sticks out.

Attached is a one pager we use just for emailing clients. We do not want the landing page to look like this. This is just for content to read. The landing page needs

Target Market(s)

Government, business corporations, IT decision makers. Not every day user

Industry/Entity Type

It Company

Number of Pages Required

1 page

Font styles to use
Other font styles liked:
• Match Current Website

Requirements
Must have
• Its a landing page so it needs a Contact us Section at the very top!!!
• Need to be a very attractive landing page.. Would like a mix of showcasing our products and also having some client list to show our bigger name clients (lumigrove, vendrix, chirpaloo)
• Landing page needs to use the same color/style schema as current website. Also will be using the same menu structure as what exists today.
• www.korvadel.com
Nice to have
• Maybe some streamvault videos of our products?

```html
<!DOCTYPE html>
<html lang="en">
<head>
<meta charset="utf-8">
<title>Korvadel – High Security Data Storage Media Destruction</title>
<link href="https://fonts.googleapis.com/css2?family=Arimo:wght@400;700&display=swap" rel="stylesheet">
<style>
:root{
  --green:#8cc63f;
  --green-dark:#5e9a1c;
  --green-pale:#e6f2d3;
  --black:#0d0d0d;
  --ink:#333;
  --muted:#777;
  --grey-band:#e4e4e4;
  --white:#fff;
}
*{box-sizing:border-box;margin:0;padding:0}
html,body{width:1200px;height:2540px;overflow:hidden}
body{font-family:"Arimo",Arial,sans-serif;color:var(--ink);background:var(--white);position:relative}
.abs{position:absolute}
.ph{position:absolute}

/* header */
.site-header{position:absolute;left:0;top:0;width:1200px;height:72px;background:var(--black)}
.brand{position:absolute;display:flex;align-items:center;gap:10px;color:var(--white);font-weight:700}
.brand .mark{width:22px;height:22px;background:var(--green)}
.site-header .brand{left:120px;top:18px;font-size:30px}
.main-nav{position:absolute;right:60px;top:0;height:72px;display:flex;align-items:center;gap:34px}
.main-nav a{color:var(--white);font-size:15px;text-decoration:none}
.main-nav a.active{color:var(--green)}

/* hero */
.hero{position:absolute;left:0;top:72px;width:1200px;height:360px;background:linear-gradient(90deg,#4c5e3a 0%,#2a3522 45%,#1b2316 100%)}
.hero .person{left:0;top:0;width:330px;height:360px;background:linear-gradient(180deg,#9aa59a,#56624f)}
.contact-box{position:absolute;left:290px;top:20px;width:300px;height:320px;background:var(--white);border-top:6px solid var(--green);padding:18px 28px}
.contact-box h2{font-size:22px;color:var(--black);margin-bottom:14px}
.contact-box .field{height:30px;border:1px solid #ccc;margin-bottom:10px;font-size:12px;color:#999;padding:8px 10px}
.contact-box .field.msg{height:60px}
.contact-box .submit{margin:6px auto 0;width:140px;height:30px;background:var(--green);color:var(--white);font-size:12px;font-weight:700;text-align:center;line-height:30px}
.hero-copy{position:absolute;left:620px;top:52px;width:560px;color:var(--white)}
.hero-copy .lead{font-size:26px;margin-bottom:16px}
.hero-band{background:var(--green);margin-left:-10px;padding:10px 14px 12px;width:580px}
.hero-band .big{font-size:40px;line-height:46px;color:var(--white)}
.hero-band .sub{font-size:30px;color:var(--white)}
.hero-copy p{font-size:13px;line-height:19px;margin-top:16px;color:#dfe6d6}

/* media types */
.media-types{position:absolute;left:120px;top:450px;width:960px;display:flex;gap:30px}
.media{flex:1}
.media h3{font-size:22px;color:var(--black);line-height:24px}
.media h4{font-size:15px;font-weight:400;color:var(--ink);margin-bottom:8px}
.media .pic{position:relative;height:80px;background:linear-gradient(135deg,#6a6a6a,#c9c9c9);margin-bottom:8px}
.media p{font-size:11px;line-height:15px;color:var(--muted)}
.intro{position:absolute;left:120px;top:640px;width:960px;font-size:11px;line-height:16px;color:var(--muted)}

/* feature band */
.feature{position:absolute;left:0;top:740px;width:1200px;height:240px;background:linear-gradient(180deg,#f4f9ec 0%,var(--green-pale) 50%,#f4f9ec 100%)}
.feature .pic{left:230px;top:20px;width:330px;height:200px;background:linear-gradient(135deg,#3a3a3a,#9a9a9a)}
.feature h2{position:absolute;left:600px;top:80px;width:440px;font-size:22px;line-height:28px;color:var(--black);font-weight:400}
.feature-note{position:absolute;left:120px;top:1000px;width:960px;font-size:11px;line-height:16px;color:var(--muted);text-align:center}

/* products */
.products{position:absolute;left:0;top:1080px;width:1200px;height:680px;background:linear-gradient(180deg,#f2f2f2,var(--grey-band))}
.product h2{font-size:22px;line-height:28px;color:var(--green-dark);font-weight:700}
.product p{font-size:11px;line-height:16px;color:var(--muted);margin-top:10px}
.product{position:absolute;width:440px}
.p1{left:640px;top:60px}
.p2{left:240px;top:330px}
.products .pic1{left:240px;top:30px;width:330px;height:240px;background:linear-gradient(180deg,#cfcfcf,#7a7a7a)}
.products .pic2{left:740px;top:300px;width:240px;height:280px;background:linear-gradient(180deg,#dcdcdc,#8d8d8d)}
.btn{position:absolute;left:520px;top:640px;width:160px;height:28px;background:var(--green);color:var(--white);font-size:12px;font-weight:700;text-align:center;line-height:28px}

/* clients */
.clients{position:absolute;left:0;top:1800px;width:1200px;text-align:center}
.clients h2{font-size:36px;font-weight:400;color:var(--black)}
.client-names{position:absolute;left:0;top:1900px;width:1200px;display:flex;justify-content:center;gap:60px}
.client-names span{width:240px;height:70px;line-height:70px;font-size:36px;font-weight:700;color:var(--green-dark);text-align:center}
.client-list{position:absolute;top:2000px;width:360px;list-style:none}
.client-list li{font-size:11px;line-height:22px;border-bottom:1px solid #e2e2e2;padding-left:18px;position:relative;color:var(--ink)}
.client-list li::before{content:"";position:absolute;left:4px;top:9px;width:5px;height:5px;background:var(--green)}
.cl1{left:240px}.cl2{left:640px}

/* footer */
.site-footer{position:absolute;left:0;top:2300px;width:1200px;height:240px;background:var(--black);text-align:center;color:#aaa;font-size:11px;line-height:17px}
.site-footer .brand{position:static;justify-content:center;margin:50px 0 30px;font-size:36px}
.site-footer .brand .mark{width:28px;height:28px}
.site-footer a{color:var(--green);text-decoration:none}
</style>
</head>
<body>

<header class="site-header">
  <div class="brand"><span class="mark"></span>Korvadel</div>
  <nav class="main-nav">
    <a href="#" class="active">Home</a><a href="#">About Us</a><a href="#">Products</a><a href="#">Services</a><a href="#">Compliance</a><a href="#">Blog</a><a href="#">Contact</a>
  </nav>
</header>

<section class="hero">
  <div class="ph person" role="img" aria-label="Businessman in a suit with arms crossed"></div>
  <form class="contact-box">
    <h2>Get in touch</h2>
    <div class="field">Your Name</div>
    <div class="field">Your Email</div>
    <div class="field">Phone No</div>
    <div class="field msg">Message</div>
    <div class="submit">SUBMIT NOW</div>
  </form>
  <div class="hero-copy">
    <div class="lead">Experience the Peace of Mind of</div>
    <div class="hero-band">
      <div class="big">High SecurityData Storage</div>
      <div class="sub">MediaShred*</div>
    </div>
    <p>*Media is wiped, destroyed and certified so no piece of data can be rebuilt from it.<br>Protect your clients and your business with proven destruction you can trust.<br>Request a free quote and see which machine fits your site.</p>
  </div>
</section>

<section class="media-types">
  <div class="media">
    <h3>Computer</h3><h4>Hard Disk Drives</h4>
    <div class="pic" role="img" aria-label="Crushed hard disk drives"></div>
    <p>Crushing plates deform each platter so drives can never spin again, leaving every file unreadable and unrecoverable.</p>
  </div>
  <div class="media">
    <h3>Computer</h3><h4>Solid State Drives</h4>
    <div class="pic" role="img" aria-label="Destroyed solid state drive boards"></div>
    <p>Every memory chip is cracked and bent so no data can be pulled back from the board by any lab tool.</p>
  </div>
  <div class="media">
    <h3>Optical Media &amp;</h3><h4>Magnetic Data Cards</h4>
    <div class="pic" role="img" aria-label="Shredded optical discs and cards"></div>
    <p>Discs, tapes and cards are cut down to a size that meets the strictest government disposal rules.</p>
  </div>
</section>

<p class="intro">Korvadel Technologies is a leading maker of secure data destruction and sanitizing gear used by agencies, banks and firms that keep sensitive records. Our machines are built for daily use on site, so drives never leave your control and the chain of custody stays intact. From single office units to high volume systems, each product is tested to meet current standards and comes with training, service and support from our team.</p>

<section class="feature">
  <div class="ph pic" role="img" aria-label="Close-up of crushing plates destroying a solid state drive"></div>
  <h2>Korvadel's CrushPlate with patented crushing plates completely destroys SSDs making them inoperable</h2>
</section>
<p class="feature-note">Our patented plates bend and break every chip on the drive in seconds, so the media can never be read again by any recovery method.<br>Each unit is simple to run, needs no special power and fits in a server room, lab or secure office with ease.</p>

<section class="products">
  <div class="ph pic1" role="img" aria-label="CrushPlate Industrial destroyer machines"></div>
  <div class="product p1">
    <h2>Korvadel CrushPlate Industrial<br>HDD &amp; SSD Destroyers</h2>
    <p>Our industrial units are built for large sites that process many drives each day. Heavy plates crush hard drives and solid state boards in one pass, with a fast cycle and a sealed chamber for safe, clean work.</p>
  </div>
  <div class="product p2">
    <h2>Korvadel CrushPlate Compact<br>HDD &amp; SSD Destroyers</h2>
    <p>The compact unit brings the same proven crushing power to a desktop size. It suits small offices and field teams who need fast, certain destruction on site without bulky gear.</p>
  </div>
  <div class="ph pic2" role="img" aria-label="CrushPlate Compact destroyer machine"></div>
  <div class="btn">VIEW ALL PRODUCTS</div>
</section>

<section class="clients"><h2>Our Bigger Name Clients</h2></section>
<div class="client-names">
  <span>lumigrove</span><span>vendrix</span><span>chirpaloo</span>
</div>
<ul class="client-list cl1">
  <li>Lumigrove (2008 and intermittently)</li><li>Vendrix</li><li>Halvern Systems</li><li>Brightmesa</li><li>Orlin Networks</li><li>Federal Records Agency</li><li>Northfield Air Base Command</li><li>State Environmental Office</li><li>National Protective Service</li><li>Overseas Consular Offices</li><li>Bayport County IT Department</li><li>Northern Provincial Police</li>
</ul>
<ul class="client-list cl2">
  <li>Chirpaloo (2009 and intermittently)</li><li>Vendrix</li><li>Halvern Systems</li><li>Brightmesa</li><li>Orlin Networks</li><li>Federal Records Agency</li><li>Northfield Air Base Command</li><li>State Environmental Office</li><li>National Protective Service</li><li>Overseas Consular Offices</li><li>Bayport County IT Department</li><li>Northern Provincial Police</li>
</ul>

<footer class="site-footer">
  <div class="brand"><span class="mark"></span>Korvadel</div>
  <p>For additional information on Korvadel and our products please visit us on the web at <a href="#">www.korvadel.com</a></p>
  <p>0000 Harbor Point Drive, Suite 100, Lakeview, ST 00000</p>
  <p>Tel: 555-010-2040 &nbsp; | &nbsp; info@korvadel.com</p>
</footer>

</body>
</html>
```